Business Book - Building Calm Habits at the Office (Less Noise, More Focus Each Day)

I'm looking for a cover that appeals to successful business people who are used to reading business titles.

The cover should feel familiar and fit in with the existing canon of bestselling business books with a vibrant, but professional look (see attached).

I want my book to stand out, but not to be frivolous. Abstract is probably best. Or close to it.

Please feel free to use my brand colours, or go with something else -

Teal
HEX #199BAB
25 / 155 / 171

Coral
HEX #EE786E
238 / 120/ 110

I don't want to include anything connected with robots or gendered assistants/business people. Or headsets.

It's only 24 hours which is mental

```html
<!DOCTYPE html>
<html lang="en">
<head>
<meta charset="utf-8">
<title>Building Calm Habits at the Office — Book Cover</title>
<link href="https://fonts.googleapis.com/css2?family=Anton&family=Roboto+Condensed:wght@400&display=swap" rel="stylesheet">
<style>
  :root {
    --coral: #EE786E;
    --ink: #0C0C0D;
    --paper: #FFFFFF;
  }
  html, body {
    margin: 0;
    padding: 0;
    width: 1200px;
    height: 1077px;
    overflow: hidden;
    background: var(--paper);
  }
  .canvas {
    position: relative;
    width: 1200px;
    height: 1077px;
  }
  .book-cover {
    position: absolute;
    left: 262px;
    top: 34px;
    width: 665px;
    height: 998px;
    background: var(--coral);
  }
  .title-panel {
    position: absolute;
    left: 322px;
    top: 122px;
    width: 545px;
    height: 736px;
    background: var(--paper);
    border-radius: 34px;
  }
  .title-art {
    position: absolute;
    left: 0;
    top: 0;
    width: 1200px;
    height: 1077px;
  }
  .title-line {
    font-family: 'Anton', 'Impact', sans-serif;
    text-transform: uppercase;
  }
  .title-line--accent { fill: var(--coral); }
  .title-line--key { fill: var(--ink); }
  .subtitle {
    position: absolute;
    left: 262px;
    top: 888px;
    width: 665px;
    margin: 0;
    text-align: center;
    color: var(--paper);
    font-family: 'Roboto Condensed', 'Arial Narrow', sans-serif;
    font-weight: 400;
    font-size: 45px;
    line-height: 48px;
    letter-spacing: 0.5px;
    text-transform: uppercase;
  }
  .subtitle span { display: block; }
</style>
</head>
<body>
<div class="canvas">
  <div class="book-cover"></div>
  <div class="title-panel"></div>

  <svg class="title-art" viewBox="0 0 1200 1077" xmlns="http://www.w3.org/2000/svg" aria-label="Building Calm Habits at the Office">
    <text class="title-line title-line--accent" x="594" y="320" font-size="169" text-anchor="middle" textLength="451" lengthAdjust="spacingAndGlyphs">Building</text>
    <text class="title-line title-line--accent" x="594" y="508" font-size="203" text-anchor="middle" textLength="451" lengthAdjust="spacingAndGlyphs">Calm</text>
    <text class="title-line title-line--accent" x="594" y="608" font-size="102" text-anchor="middle" textLength="451" lengthAdjust="spacingAndGlyphs">Habits at the</text>
    <text class="title-line title-line--key" x="594" y="800" font-size="208" text-anchor="middle" textLength="451" lengthAdjust="spacingAndGlyphs">Office</text>
  </svg>

  <p class="subtitle">
    <span>Less Noise, More Focus</span>
    <span>Each Day</span>
  </p>
</div>
</body>
</html>
```